Banner Design for High End Jewelry Website

We need a banner for our website (brindlestone.com) for a sale that we will be running. The banner should be a size 1187 × 400. I have included a few pieces of jewelry to be included in the banner (do not need to use all, can use just some). The banner should say:
"Christmas is Closer Than You Think Sale!"
Shop Now

Industry/Entity Type

Jewelry

```html
<!DOCTYPE html>
<html lang="en">
<head>
<meta charset="UTF-8">
<title>Brindlestone Christmas Sale Banner</title>
<link href="https://fonts.googleapis.com/css2?family=Arimo:wght@400&display=swap" rel="stylesheet">
<style>
  :root {
    --stage: #000000;
    --champagne-light: #f4ecdd;
    --champagne-mid: #e8dcc4;
    --champagne-deep: #d9c8a6;
    --wine: #74253f;
    --wine-dark: #6a203a;
    --link: #4d2030;
    --gold-soft: #cdb36a;
    --gold-muted: #a8955f;
    --jewel-shade: #7d7560;
  }
  * { margin: 0; padding: 0; box-sizing: border-box; }
  html, body {
    width: 1200px;
    height: 610px;
    overflow: hidden;
    background: var(--stage);
  }
  .sale-banner {
    position: absolute;
    left: 48px;
    top: 118px;
    width: 1103px;
    height: 373px;
    overflow: hidden;
    background:
      radial-gradient(ellipse 560px 320px at 70% 60%, var(--champagne-light) 0%, rgba(244,236,221,0) 100%),
      linear-gradient(180deg, var(--champagne-deep) 0%, var(--champagne-mid) 55%, var(--champagne-light) 100%);
    font-family: "Arimo", "Helvetica Neue", Arial, sans-serif;
  }
  .sale-banner__headline {
    position: absolute;
    left: 113px;
    top: 44px;
    color: var(--wine);
    font-size: 35px;
    font-weight: 400;
    line-height: 51px;
    letter-spacing: -0.6px;
  }
  .sale-banner__title {
    position: absolute;
    left: 103px;
    top: 146px;
    color: var(--wine-dark);
    font-size: 168px;
    font-weight: 400;
    line-height: 1;
    letter-spacing: -7px;
    text-shadow: 0 2px 3px rgba(80, 40, 30, 0.25);
  }
  .sale-banner__jewelry {
    position: absolute;
    left: 609px;
    top: 112px;
    width: 330px;
    height: 196px;
    border-radius: 24px;
    background: linear-gradient(160deg, var(--gold-soft) 0%, var(--gold-muted) 55%, var(--jewel-shade) 100%);
  }
  .sale-banner__cta {
    position: absolute;
    left: 955px;
    top: 324px;
    display: flex;
    align-items: center;
    gap: 6px;
    color: var(--link);
    font-size: 19px;
    letter-spacing: -0.5px;
    text-decoration: none;
  }
  .sale-banner__cta-icon { width: 19px; height: 19px; display: block; }
</style>
</head>
<body>
  <section class="sale-banner">
    <h2 class="sale-banner__headline">Christmas is Closer<br>Than You Think</h2>
    <h1 class="sale-banner__title">Sale!</h1>
    <div class="sale-banner__jewelry" role="img" aria-label="Product photo: pair of gold floral earrings with pink stone centres"></div>
    <a class="sale-banner__cta" href="#">
      <span>Shop Now</span>
      <svg class="sale-banner__cta-icon" viewBox="0 0 20 20" aria-hidden="true">
        <circle cx="10" cy="10" r="9.5" fill="var(--wine)"/>
        <path d="M8 5.8 L14 10 L8 14.2 Z" fill="#ffffff"/>
      </svg>
    </a>
  </section>
</body>
</html>
```